Grand Bridal Pastry Selling Method needs finishing touches to website.

We have a temporary website located at http://www.brivantaworks.example/qk/.
We are doing a responsive design and have created the architecture (layout). However, we need a professional makeover for the graphic elements and colors of the website. The website will be selling a sales course to mostly women who sell wedding cakes.
The photos within the posted website are for illustrative purposes. We will use our own photos after the website is redone.
We are open to changing the font styles, borders, header, and anything else as long as the layout is not changed.
Target Market(s)
75% women age 25-50 and men 30-60.
Industry/Entity Type
Architecture
Colors
Designer to choose colors to be used in the design.
Look and feel
Each slider illustrates characteristics of the customer's brand and the style your logo design should communicate.

```html
<!DOCTYPE html>
<html lang="en">
<head>
<meta charset="utf-8">
<title>Grand Bridal Pastry Selling Method</title>
<link rel="stylesheet" href="https://fonts.googleapis.com/css2?family=Oswald:wght@400;500&family=Open+Sans:wght@400;700&family=Oxygen:wght@300;400;700&display=swap">
<style>
:root{
  --green:#6eaa35;
  --green-light:#8cc653;
  --green-dark:#3f6f1d;
  --green-text:#6aa632;
  --grey-nav:#555;
  --band:#eeeced;
  --band-2:#e4e4e4;
  --footer:#3b3b3b;
  --ink:#222;
  --logo-grey:#a7a7a7;
}
*{margin:0;padding:0;box-sizing:border-box}
html,body{width:1200px;height:1069px;overflow:hidden;background:#fff}
body{position:relative;font-family:"Open Sans",sans-serif;color:var(--ink)}
.abs{position:absolute}

.header{left:0;top:0;width:1200px;height:78px;background:#fff;box-shadow:0 2px 3px rgba(0,0,0,.15);z-index:2}
.brand{left:180px;top:26px;font-family:"Oswald",sans-serif;font-weight:500;font-size:22px;color:var(--green-text);letter-spacing:.3px}
.nav{position:absolute;right:182px;top:40px;display:flex;gap:24px}
.nav a{font-family:"Oxygen",sans-serif;font-size:13.5px;color:var(--grey-nav);text-decoration:none;white-space:nowrap}
.nav a.active{color:var(--green-text)}

.hero{left:0;top:78px;width:1200px;height:381px;background:radial-gradient(circle at 930px 210px,var(--green-light) 0,var(--green) 260px)}
.video{left:224px;top:113px;width:407px;height:297px;background:linear-gradient(160deg,#5d564f,#2d2a27 60%,#1a1817);border-top:12px solid #111;border-bottom:14px solid #222}
.video .play{position:absolute;left:157px;top:116px;width:72px;height:50px;border-radius:12px;background:#d21f1f}
.video .play svg{position:absolute;left:25px;top:14px}
.offer{left:678px;top:131px;width:350px;font-weight:700;font-size:18.5px;line-height:21.5px;color:#fff;text-transform:uppercase}
.field{left:678px;width:161px;height:47px;background:#fff;padding:0 15px;font-family:"Oxygen",sans-serif;font-size:12px;color:#aaa;line-height:47px}
.cta{left:678px;top:337px;width:151px;height:40px;border-radius:5px;background:var(--green-dark);box-shadow:3px 3px 0 #5b8f2d;color:#fff;font-family:"Oswald",sans-serif;font-size:14px;line-height:40px;text-align:center;letter-spacing:-.3px}

.tagline-band{left:0;top:459px;width:1200px;height:102px;background:var(--band)}
.tagline{left:310px;top:491px;font-family:"Oswald",sans-serif;font-weight:500;font-size:22px;letter-spacing:-.6px;color:#333}
.spacer-band{left:0;top:561px;width:1200px;height:54px;background:var(--band-2)}
.cake-left{left:210px;top:429px;width:77px;height:120px;border-radius:8px;background:linear-gradient(#9bc86a,#f4eee4 40%,#e8e2d6)}
.cake-right{left:836px;top:373px;width:137px;height:171px;border-radius:40% 40% 30% 30%;background:linear-gradient(#f7f7f7,#ececec 70%,#9fd2d8)}

.card h3{font-family:"Oxygen",sans-serif;font-weight:400;font-size:16px;line-height:19px;color:#333}
.card h3 b{display:block;font-weight:700;font-size:19px;line-height:22.5px;color:var(--green-text);margin-top:2px}
.card p{font-family:"Open Sans",sans-serif;font-size:11.2px;line-height:13.7px;color:#222;margin-top:14px}
.card .more{position:absolute;left:0;width:69px;height:28px;border-radius:14px;background:var(--green);color:#fff;font-size:11px;line-height:28px;text-align:center}
.divider{top:629px;width:1px;height:188px;background:#ddd}
.photo{border-radius:6px}

.press{left:0;top:841px;width:1200px;height:126px;background:var(--band)}
.badge{top:885px;height:37px;background:var(--logo-grey);opacity:.75}

.footer{left:0;top:967px;width:1200px;height:102px;background:var(--footer)}
.fnav a{position:absolute;top:1005px;color:#fff;font-size:12px;text-decoration:none;white-space:nowrap}
.copy{left:181px;top:1031px;color:#fff;font-size:12px;white-space:nowrap}
.social{top:1013px;width:32px;height:32px;border-radius:3px}
</style>
</head>
<body>

<header class="abs header">
  <div class="abs brand">BRIVANTAWORKS</div>
  <nav class="nav">
    <a class="active">HOME</a>
    <a>WHO IS LON VARRICK</a>
    <a>WHY LON IS SHARING HIS SECRETS</a>
    <a>CONTACT</a>
  </nav>
</header>

<section class="abs hero"></section>
<div class="abs video" role="img" aria-label="Embedded video: photo booth product showcase">
  <div class="play"><svg width="22" height="22" viewBox="0 0 22 22"><path d="M3 1 L20 11 L3 21 Z" fill="#fff"/></svg></div>
</div>
<h2 class="abs offer">Free videos to help you sell more wedding cakes at higher prices... immediately</h2>
<div class="abs field" style="top:211px">ENTER YOUR NAME</div>
<div class="abs field" style="top:271px">ENTER YOUR MAIL ID</div>
<div class="abs cta">GET INSTANT ACCESS</div>

<section class="abs tagline-band"></section>
<section class="abs spacer-band"></section>
<div class="abs cake-left" role="img" aria-label="Photo of a flower-decorated tiered wedding cake"></div>
<div class="abs cake-right" role="img" aria-label="Photo of a white tiered wedding cake with teal hearts"></div>
<h2 class="abs tagline">3 Leading-Edge Techniques for Convincing Brides to Choose You</h2>

<article class="abs card" style="left:180px;top:637px;width:140px">
  <h3 style="width:140px">Two Faces Of Your<b>Wedding Cake Business</b></h3>
  <p>One side of your face displays your "Internal Reality." It's how you run your business. Whether...</p>
</article>
<div class="abs card" style="left:180px;top:787px"><span class="more">Read More</span></div>
<div class="abs photo" style="left:330px;top:638px;width:81px;height:125px;background:linear-gradient(#f2f0ea,#dcd8cf)" role="img" aria-label="Photo of a tall white wedding cake with couple topper"></div>
<div class="abs divider" style="left:440px"></div>

<article class="abs card" style="left:472px;top:637px;width:145px">
  <h3 style="width:100px">The<b>Insecurity Gap</b></h3>
  <p>The #1 Reason You're Not Selling More Wedding Cakes...is due to "The Insecurity Gap" a bride...</p>
</article>
<div class="abs card" style="left:472px;top:787px"><span class="more">Read More</span></div>
<div class="abs photo" style="left:634px;top:624px;width:86px;height:156px;background:linear-gradient(#8a5a3c,#9a9aa4 45%,#e8e8ea)" role="img" aria-label="Photo of a confident businesswoman with arms crossed"></div>
<div class="abs divider" style="left:739px"></div>

<article class="abs card" style="left:755px;top:637px;width:150px">
  <h3 style="width:135px">External Perception to WIN more.<b>wedding cake orders</b></h3>
  <p style="margin-top:14px">Start thinking in terms of being the "World's</p>
</article>
<div class="abs card" style="left:755px;top:787px"><span class="more">Read More</span></div>
<div class="abs photo" style="left:917px;top:624px;width:86px;height:169px;background:linear-gradient(#e2c890,#efe6d6 45%,#f6f1e8)" role="img" aria-label="Photo of a thoughtful smiling businesswoman"></div>

<section class="abs press"></section>
<div class="abs badge" style="left:232px;width:37px" role="img" aria-label="Press mention badge"></div>
<div class="abs badge" style="left:327px;width:117px;height:20px;top:894px" role="img" aria-label="Press mention badge"></div>
<div class="abs badge" style="left:504px;width:36px;border-radius:50%" role="img" aria-label="Press mention badge"></div>
<div class="abs badge" style="left:639px;width:43px" role="img" aria-label="Press mention badge"></div>
<div class="abs badge" style="left:750px;width:94px" role="img" aria-label="Press mention badge"></div>
<div class="abs badge" style="left:896px;width:80px" role="img" aria-label="Press mention badge"></div>

<footer class="abs footer"></footer>
<nav class="fnav">
  <a style="left:181px">Home</a>
  <a style="left:233px">Who Is Lon Varrick</a>
  <a style="left:356px">Why Lon Is Sharing His Secrets</a>
  <a style="left:544px">Contact</a>
</nav>
<div class="abs copy">Copyright © 2014 The Sugar Atelier. Phone: 555.014.2290. All Rights Reserved.</div>
<div class="abs social" style="left:840px;background:#f2b82a" role="img" aria-label="Feed link"></div>
<div class="abs social" style="left:890px;background:#6cc1e8" role="img" aria-label="Social link"></div>
<div class="abs social" style="left:939px;background:#e27aa4" role="img" aria-label="Social link"></div>
<div class="abs social" style="left:990px;background:#3d63b0" role="img" aria-label="Social link"></div>

</body>
</html>
```